Valtrexo inc. Stationery
Need Letter Head, Small Envelop, A4 Env, Biz Card, folder, Power Point Templet and Email signature
Valtrexo inc. Stationery - Telecommunications
Creative Brief
Use same font as used in my logo
Gilles Montreuil
PDG/CEO
2384, rue Dufresnay Saint-Colomban, Québec Canada, K4P 2B7
gillesmontreuil@valtrexo.ca
www.valtrexo.ca
RBQ: 4817-2039-56
Please use icons for phone, cell, email ect.

```html
<!DOCTYPE html>
<html lang="fr">
<head>
<meta charset="utf-8">
<title>Valtrexo inc. – Stationery</title>
<link href="https://fonts.googleapis.com/css2?family=Montserrat:wght@400;600;700&display=swap" rel="stylesheet">
<style>
  :root {
    --bg: #e9ecef;
    --paper: #ffffff;
    --blue-deep: #0f3f7a;
    --blue: #1f64b3;
    --blue-light: #4f93d6;
    --ink: #2b3440;
    --ink-soft: #6b7684;
    --faint: #dbe7f3;
  }
  * { box-sizing: border-box; margin: 0; padding: 0; }
  html, body { width: 1200px; height: 794px; overflow: hidden; }
  body {
    background: var(--bg);
    font-family: "Montserrat", sans-serif;
    color: var(--ink);
    position: relative;
  }
  .sheet { position: absolute; background: var(--paper); box-shadow: 0 6px 18px rgba(20,40,70,.14); overflow: hidden; }
  .brand { font-weight: 700; letter-spacing: .01em; display: flex; align-items: center; gap: 6px; }
  .brand .dot { width: .8em; height: .8em; border-radius: 50%; background: currentColor; display: inline-block; }
  .brand--blue { color: var(--blue); }
  .brand--white { color: var(--paper); }
  .band { position: absolute; left: 0; width: 100%; }
  .band svg { display: block; width: 100%; height: 100%; }
  .decor-circle { position: absolute; border-radius: 50%; }

  /* Letterhead */
  .letterhead { left: 40px; top: 40px; width: 300px; height: 390px; }
  .letterhead .brand { position: absolute; top: 18px; left: 50%; transform: translateX(-50%); font-size: 17px; }
  .letterhead .decor-circle { width: 110px; height: 110px; left: 95px; top: 60px; background: var(--faint); opacity: .7; }
  .letterhead .band { bottom: 0; height: 70px; }
  .letterhead .footer { position: absolute; bottom: 10px; left: 0; width: 100%; text-align: center; color: var(--paper); font-size: 6.5px; line-height: 1.6; }

  /* Folder */
  .folder { left: 370px; top: 40px; width: 310px; height: 420px;
    background: linear-gradient(160deg, var(--blue-light) 0%, var(--blue) 45%, var(--blue-deep) 100%); }
  .folder .brand { position: absolute; top: 58px; left: 50%; transform: translateX(-50%); font-size: 30px; }
  .folder .tagline { position: absolute; top: 100px; width: 100%; text-align: center; color: var(--faint); font-size: 8px; letter-spacing: .18em; text-transform: uppercase; }
  .folder .decor-circle { width: 170px; height: 170px; left: 70px; top: 200px; background: rgba(255,255,255,.12); }

  /* Business cards */
  .card { width: 330px; height: 190px; left: 710px; }
  .card--front { top: 40px; background: linear-gradient(150deg, var(--blue) 0%, var(--blue-deep) 100%); }
  .card--front .brand { position: absolute; top: 50%; left: 50%; transform: translate(-50%,-50%); font-size: 28px; }
  .card--back { top: 250px; padding: 22px 24px; }
  .card--back .brand { font-size: 15px; margin-bottom: 14px; }
  .person-name { font-size: 14px; font-weight: 600; color: var(--blue-deep); }
  .person-role { font-size: 9px; color: var(--ink-soft); margin-bottom: 10px; letter-spacing: .08em; }
  .contact-list { list-style: none; font-size: 8.5px; line-height: 1.75; }
  .contact-list li { display: flex; align-items: center; gap: 7px; }
  .contact-list svg { width: 10px; height: 10px; fill: var(--blue); flex: none; }
  .card--back .band { bottom: 0; height: 14px; background: linear-gradient(90deg, var(--blue-deep), var(--blue)); }

  /* Envelopes */
  .envelope { top: 500px; height: 250px; }
  .envelope--dl { left: 40px; width: 520px; }
  .envelope--dl .band { top: 0; height: 70px; }
  .envelope--dl .brand { position: absolute; top: 84px; left: 26px; font-size: 20px; }
  .envelope--dl .sender { position: absolute; top: 116px; left: 26px; font-size: 8px; line-height: 1.6; color: var(--ink-soft); }
  .envelope--large { left: 600px; width: 560px; }
  .envelope--large .band { top: 0; height: 110px; }
  .envelope--large .brand { position: absolute; top: 36px; left: 50%; transform: translateX(-50%); font-size: 24px; }
  .envelope--large .sender { position: absolute; bottom: 22px; left: 28px; font-size: 8px; line-height: 1.6; color: var(--ink-soft); }
</style>
</head>
<body>

<svg width="0" height="0" style="position:absolute">
  <defs>
    <linearGradient id="bandGradient" x1="0" y1="0" x2="1" y2="1">
      <stop offset="0" stop-color="#4f93d6"/>
      <stop offset=".5" stop-color="#1f64b3"/>
      <stop offset="1" stop-color="#0f3f7a"/>
    </linearGradient>
    <symbol id="icon-phone" viewBox="0 0 24 24"><path d="M6.6 10.8a15 15 0 0 0 6.6 6.6l2.2-2.2c.3-.3.7-.4 1-.2 1.1.4 2.3.6 3.6.6.6 0 1 .4 1 1V20c0 .6-.4 1-1 1A17 17 0 0 1 3 4c0-.6.4-1 1-1h3.5c.6 0 1 .4 1 1 0 1.3.2 2.5.6 3.6.1.3 0 .7-.2 1z"/></symbol>
    <symbol id="icon-cell" viewBox="0 0 24 24"><path d="M7 1h10a2 2 0 0 1 2 2v18a2 2 0 0 1-2 2H7a2 2 0 0 1-2-2V3a2 2 0 0 1 2-2zm0 3v14h10V4zm5 15.5a1.2 1.2 0 1 0 0 2.4 1.2 1.2 0 0 0 0-2.4z"/></symbol>
    <symbol id="icon-mail" viewBox="0 0 24 24"><path d="M2 4h20v16H2zm2 2v.5l8 5 8-5V6zm0 2.8V18h16V8.8l-8 5z"/></symbol>
    <symbol id="icon-web" viewBox="0 0 24 24"><path d="M12 2a10 10 0 1 0 0 20 10 10 0 0 0 0-20zm0 2c.9 1.2 1.6 2.6 2 4h-4c.4-1.4 1.1-2.8 2-4zM4.3 14a8 8 0 0 1 0-4h3.4a16 16 0 0 0 0 4zm.8 2h3c.3 1.3.8 2.5 1.4 3.6A8 8 0 0 1 5.1 16zm3-8h-3a8 8 0 0 1 4.4-3.6C7.9 5.5 7.4 6.7 8.1 8zM12 20c-.9-1.2-1.6-2.6-2-4h4c-.4 1.4-1.1 2.8-2 4zm2.3-6H9.7a14 14 0 0 1 0-4h4.6a14 14 0 0 1 0 4zm.2 5.6c.6-1.1 1.1-2.3 1.4-3.6h3a8 8 0 0 1-4.4 3.6zM16.3 14a16 16 0 0 0 0-4h3.4a8 8 0 0 1 0 4zm-.4-6c-.3-1.3-.8-2.5-1.4-3.6A8 8 0 0 1 18.9 8z"/></symbol>
    <symbol id="icon-pin" viewBox="0 0 24 24"><path d="M12 2a7 7 0 0 0-7 7c0 5 7 13 7 13s7-8 7-13a7 7 0 0 0-7-7zm0 9.5a2.5 2.5 0 1 1 0-5 2.5 2.5 0 0 1 0 5z"/></symbol>
  </defs>
</svg>

<!-- Letterhead -->
<section class="sheet letterhead" aria-label="Letterhead">
  <div class="brand brand--blue"><span class="dot"></span>Valtrexo</div>
  <div class="decor-circle" aria-hidden="true"></div>
  <div class="band" role="img" aria-label="Blue textured wave band">
    <svg viewBox="0 0 300 70" preserveAspectRatio="none"><path d="M0 22 Q150 -6 300 18 L300 70 L0 70 Z" fill="url(#bandGradient)"/></svg>
  </div>
  <p class="footer">2384, rue Dufresnay, Saint-Colomban, Québec Canada, K4P 2B7<br>gillesmontreuil@valtrexo.ca · www.valtrexo.ca · RBQ: 4817-2039-56</p>
</section>

<!-- Folder -->
<section class="sheet folder" role="img" aria-label="Presentation folder with blue textured gradient">
  <div class="brand brand--white"><span class="dot"></span>Valtrexo</div>
  <p class="tagline">Connecting your business</p>
  <div class="decor-circle" aria-hidden="true"></div>
</section>

<!-- Business card front -->
<section class="sheet card card--front" aria-label="Business card front">
  <div class="brand brand--white"><span class="dot"></span>Valtrexo</div>
</section>

<!-- Business card back -->
<section class="sheet card card--back" aria-label="Business card back">
  <div class="brand brand--blue"><span class="dot"></span>Valtrexo</div>
  <p class="person-name">Gilles Montreuil</p>
  <p class="person-role">PDG/CEO</p>
  <ul class="contact-list">
    <li><svg><use href="#icon-pin"/></svg>2384, rue Dufresnay, Saint-Colomban, Québec, K4P 2B7</li>
    <li><svg><use href="#icon-mail"/></svg>gillesmontreuil@valtrexo.ca</li>
    <li><svg><use href="#icon-web"/></svg>www.valtrexo.ca</li>
  </ul>
  <div class="band" aria-hidden="true"></div>
</section>

<!-- DL envelope -->
<section class="sheet envelope envelope--dl" aria-label="Small envelope">
  <div class="band" role="img" aria-label="Blue textured wave band">
    <svg viewBox="0 0 520 70" preserveAspectRatio="none"><path d="M0 0 L520 0 L520 40 Q260 78 0 50 Z" fill="url(#bandGradient)"/></svg>
  </div>
  <div class="brand brand--blue"><span class="dot"></span>Valtrexo</div>
  <p class="sender">Valtrexo inc.<br>2384, rue Dufresnay<br>Saint-Colomban, Québec Canada, K4P 2B7</p>
</section>

<!-- Large envelope -->
<section class="sheet envelope envelope--large" aria-label="Large envelope">
  <div class="band" role="img" aria-label="Blue textured wave band">
    <svg viewBox="0 0 560 110" preserveAspectRatio="none"><path d="M0 0 L560 0 L560 80 Q280 120 0 90 Z" fill="url(#bandGradient)"/></svg>
  </div>
  <div class="brand brand--white"><span class="dot"></span>Valtrexo</div>
  <p class="sender">Valtrexo inc. · 2384, rue Dufresnay, Saint-Colomban, Québec Canada, K4P 2B7<br>www.valtrexo.ca</p>
</section>

</body>
</html>
```